Brevik Seasoning
Brevik Seasoning - Food
Creative Brief
Simple
Tom Halvern
President and CEO
52190 Harlow Lane Dunmore Falls, OH 48977
thalvern@brevikspice.com
Brevikspice.com
Xpert Xpert

```html
<!DOCTYPE html>
<html lang="en">
<head>
<meta charset="utf-8">
<title>Brevik Seasoning – Business Cards</title>
<link rel="stylesheet" href="https://fonts.googleapis.com/css2?family=Open+Sans:wght@400;600&display=swap">
<style>
  :root {
    --backdrop: #e9e6e2;
    --card: #ffffff;
    --ink: #1d1d1d;
    --muted: #3a3a3a;
    --accent-red: #c8102e;
    --soft-grey: #d9d9d9;
    --deep: #151515;
    --faint: #ece9e6;
  }
  * { margin: 0; padding: 0; box-sizing: border-box; }
  html, body { width: 1200px; height: 904px; overflow: hidden; }
  body {
    background: var(--backdrop);
    font-family: "Open Sans", Arial, sans-serif;
    color: var(--ink);
    position: relative;
  }
  .card {
    position: absolute;
    width: 520px;
    height: 300px;
    background: var(--card);
    border-radius: 18px;
    overflow: hidden;
    box-shadow: 0 6px 18px rgba(0,0,0,0.18);
  }
  .card--front { left: 70px; top: 150px; }
  .card--back { left: 610px; top: 454px; }

  .front-mark {
    position: absolute;
    left: 0; right: 0; top: 118px;
    text-align: center;
    font-size: 46px;
    font-weight: 600;
    color: var(--faint);
    letter-spacing: 1px;
  }

  .wordmark {
    position: absolute;
    left: 30px; top: 112px;
    display: flex; align-items: center; gap: 8px;
    font-size: 19px; font-weight: 600; color: var(--ink);
    white-space: nowrap;
  }
  .wordmark-dot {
    width: 12px; height: 12px; border-radius: 50%;
    background: var(--accent-red);
  }

  .holder { position: absolute; left: 258px; top: 22px; }
  .holder-name { font-size: 22px; font-weight: 400; color: var(--ink); line-height: 1.1; }
  .holder-title { font-size: 9px; font-weight: 600; color: var(--accent-red); margin-top: 2px; }

  .contact-list {
    position: absolute; left: 270px; top: 74px;
    list-style: none; font-size: 11px; color: var(--muted); line-height: 1.3;
  }
  .contact-list li { display: flex; align-items: flex-start; gap: 10px; margin-bottom: 4px; }
  .contact-list svg { width: 11px; height: 11px; flex: none; margin-top: 2px; fill: var(--ink); }

  .swoosh { position: absolute; left: 0; bottom: 0; width: 520px; height: 130px; }
</style>
</head>
<body>
  <section class="card card--front" aria-label="Card front">
    <div class="front-mark">Brevik Seasoning</div>
  </section>

  <section class="card card--back" aria-label="Card back">
    <div class="holder">
      <div class="holder-name">Tom Halvern</div>
      <div class="holder-title">President and CEO</div>
    </div>

    <ul class="contact-list">
      <li>
        <svg viewBox="0 0 12 12"><path d="M6 0a4 4 0 0 0-4 4c0 3 4 8 4 8s4-5 4-8a4 4 0 0 0-4-4zm0 5.5a1.5 1.5 0 1 1 0-3 1.5 1.5 0 0 1 0 3z"/></svg>
        <span>52190 Harlow Lane<br>Dunmore Falls, OH 48977</span>
      </li>
      <li>
        <svg viewBox="0 0 12 12"><rect x="1" y="4" width="10" height="7" rx="1"/><rect x="2" y="1" width="8" height="3" rx="1"/></svg>
        <span>614-555-0147</span>
      </li>
      <li>
        <svg viewBox="0 0 12 12"><rect x="3" y="0" width="6" height="12" rx="1"/></svg>
        <span>937-555-0182</span>
      </li>
      <li>
        <svg viewBox="0 0 12 12"><rect x="0" y="2" width="12" height="8" rx="1"/><path d="M0 2.5l6 4 6-4" stroke="#fff" stroke-width="1" fill="none"/></svg>
        <span>thalvern@brevikspice.com</span>
      </li>
      <li>
        <svg viewBox="0 0 12 12"><circle cx="6" cy="6" r="5.5"/><path d="M0.5 6h11M6 0.5v11M6 0.5c-3 3-3 8 0 11M6 0.5c3 3 3 8 0 11" stroke="#fff" stroke-width="0.8" fill="none"/></svg>
        <span>Brevikspice.com</span>
      </li>
    </ul>

    <div class="wordmark">
      <span class="wordmark-dot"></span>
      <span>Brevik Seasoning</span>
    </div>

    <svg class="swoosh" viewBox="0 0 520 130" preserveAspectRatio="none" aria-hidden="true">
      <path d="M0 40 C 140 110, 300 120, 520 0 L520 130 L0 130 Z" fill="var(--accent-red)"/>
      <path d="M0 50 C 140 118, 300 128, 520 10 L520 130 L0 130 Z" fill="var(--soft-grey)"/>
      <path d="M0 60 C 140 126, 300 134, 520 22 L520 130 L0 130 Z" fill="var(--card)"/>
      <path d="M0 120 C 180 95, 360 100, 520 112 L520 130 L0 130 Z" fill="var(--accent-red)"/>
    </svg>
  </section>
</body>
</html>
```